Looking for a full stationery set design for our business - NO generic/stock templates please.

I am looking for a complete stationary set for my used car dealership. I am looking for something, unique, creative, classy and high-end. Generic designs or anything that looks like a 'stock' template will not be selected. Please do not use a vehicle image in the design - - that is too predictable for a car dealership.

I prefer matte designs over shiny/glossy designs but will consider both if the look is right. I have attached a few different variations of our logo you can work with, as well as a QR code to our website.

These are the items needed:
- Letterhead (with MS word file)
- Envelope #10
- Envelope 9" x 12"
- Envelope 10" x 13"
- Presentation Folder 9" x 12"
- Business Cards 2" x 3.5"
- Folded Card (5.5 x 8" folded to 4" x 5.5")
- Notepad Small (4" x 6")
- Notepad Large (5.5" x 8.5")
- Postcard (4" x 6")

Low design entries Many entries from the same designers Many repetitive designs Too many generic entries that look like stock templates

• Original, creative work, high-end/classy appeal. Must stand out as high-quality, professional image that captures your attention.
• No generic/stock templates or anything that looks like it.

```html
<!DOCTYPE html>
<html lang="en">
<head>
<meta charset="utf-8">
<title>Northgate Motors Stationery</title>
<link rel="stylesheet" href="https://fonts.googleapis.com/css2?family=Open+Sans:wght@400;600;800&family=Great+Vibes&display=swap">
<style>
  :root{
    --blue:#1e7fc9;
    --ink:#262626;
    --dark:#222222;
    --paper:#ffffff;
    --rule:#d9d9d9;
    --text:#4a4a4a;
    --bg:#ececec;
  }
  *{box-sizing:border-box;margin:0;padding:0}
  html,body{width:1200px;height:1200px;overflow:hidden}
  body{background:var(--bg);font-family:"Open Sans",Arial,sans-serif;color:var(--text);position:relative}
  .piece{position:absolute;background:var(--paper);overflow:hidden}
  .brand{font-family:"Open Sans",Arial,sans-serif;font-weight:800;color:var(--ink);white-space:nowrap;letter-spacing:-0.3px;line-height:1;display:flex;align-items:center;gap:5px}
  .brand .dot{display:inline-block;background:var(--blue);border-radius:50%}
  .brand.light{color:#ffffff}
  .foot-blue{position:absolute;left:0;right:0;bottom:0;background:var(--blue)}
  .foot-dark{position:absolute;right:0;bottom:0;background:var(--dark);color:#fff;display:flex;align-items:center;justify-content:flex-end;letter-spacing:2px;clip-path:polygon(14px 0,100% 0,100% 100%,0 100%)}
  .ico{display:inline-block;border-radius:50%;border:1.5px solid var(--blue);vertical-align:middle;margin-right:4px}
  .contact{position:absolute;line-height:1.45;color:var(--ink)}

  /* business card front */
  .card-front{left:166px;top:168px;width:277px;height:158px}
  .card-front .brand{position:absolute;right:24px;top:28px;font-size:15px}
  .card-front .name{position:absolute;left:22px;top:84px;font-size:10.5px;color:var(--ink)}
  .card-front .name b{font-weight:400;color:var(--blue)}
  .card-front .role{position:absolute;left:22px;top:98px;font-size:6px;color:var(--text)}
  .card-front .divider{position:absolute;left:22px;right:17px;top:110px;height:1px;background:#bdbdbd}
  .card-front .contact{font-size:6px}
  .card-front .c-left{left:22px;top:115px}
  .card-front .c-right{right:17px;top:115px;text-align:right}
  .card-front .foot-blue{height:7px}
  .card-front .foot-dark{width:132px;height:18px}

  /* business card back */
  .card-back{left:464px;top:168px;width:277px;height:158px;background:var(--dark)}
  .card-back .brand{position:absolute;left:0;right:0;top:66px;justify-content:center;font-size:24px}

  /* notepad */
  .notepad{left:820px;top:134px;width:258px;height:384px}
  .notepad .brand{position:absolute;left:0;right:0;top:25px;justify-content:center;font-size:13px}
  .notepad .lines{position:absolute;left:22px;right:21px;top:78px}
  .notepad .lines span{display:block;height:25px;border-top:1px solid var(--rule)}
  .notepad .contact{font-size:3.6px;top:366px}
  .notepad .c-left{left:9px}
  .notepad .c-right{left:70px;padding-left:5px;border-left:1px solid #bbb}
  .notepad .foot-blue{height:3px}
  .notepad .foot-dark{width:88px;height:9px;font-size:3.8px;padding-right:8px;letter-spacing:1px;clip-path:polygon(8px 0,100% 0,100% 100%,0 100%)}

  /* letterhead back */
  .letter-back{left:110px;top:370px;width:516px;height:696px;background:var(--dark)}
  .letter-back .brand{position:absolute;left:0;right:0;top:40px;justify-content:center;font-size:30px}
  .letter-back .contact{left:18px;top:659px;font-size:8.5px;color:#fff}
  .letter-back .ico{border-color:#fff;background:var(--blue)}
  .letter-back .foot-blue{height:8px}

  /* letterhead front */
  .letter{left:188px;top:420px;width:477px;height:672px}
  .letter .brand{position:absolute;left:33px;top:34px;font-size:17px}
  .letter .body{position:absolute;left:64px;width:356px;font-size:7.6px;line-height:13.5px;color:var(--text)}
  .letter .salute{top:142px}
  .letter .p1{top:195px}
  .letter .p2{top:303px}
  .letter .p3{top:397px}
  .letter .body p{text-align:justify}
  .letter .closing{position:absolute;left:66px;top:509px;font-size:7.6px}
  .letter .sign{position:absolute;left:64px;top:522px;font-family:"Great Vibes",cursive;font-size:30px;color:var(--blue)}
  .letter .contact{font-size:7.5px;top:638px}
  .letter .c-left{left:17px}
  .letter .c-right{left:124px;padding-left:6px;border-left:1px solid #bbb}
  .letter .foot-blue{height:6px}
  .letter .foot-dark{width:170px;height:17px;font-size:7px;padding-right:14px}

  /* letterhead second sheet */
  .sheet{left:698px;top:548px;width:414px;height:544px}
  .sheet .brand{position:absolute;left:28px;top:38px;font-size:16px}
  .sheet .contact{left:16px;top:522px;font-size:7.2px}
  .sheet .foot-blue{height:6px}
  .sheet .foot-dark{width:144px;height:15px;font-size:6.5px;padding-right:12px}
</style>
</head>
<body>

<section class="piece card-front">
  <div class="brand"><span class="dot" style="width:7px;height:7px"></span>Northgate Motors</div>
  <div class="name"><b>JOHN</b> DOE</div>
  <div class="role">Director</div>
  <div class="divider"></div>
  <div class="contact c-left">
    <div><span class="ico" style="width:5px;height:5px"></span>000.000.0000</div>
    <div><span class="ico" style="width:5px;height:5px"></span>www.northgatemotors.com</div>
    <div><span class="ico" style="width:5px;height:5px"></span>john@northgatemotors.com</div>
  </div>
  <div class="contact c-right">
    <div>Dummy city <span class="ico" style="width:5px;height:5px;margin:0 0 0 3px"></span></div>
    <div>Dummy country, land</div>
  </div>
  <div class="foot-blue"></div>
  <div class="foot-dark"></div>
</section>

<section class="piece card-back">
  <div class="brand light"><span class="dot" style="width:10px;height:10px"></span>Northgate Motors</div>
</section>

<section class="piece notepad">
  <div class="brand"><span class="dot" style="width:6px;height:6px"></span>Northgate Motors</div>
  <div class="lines"><span></span><span></span><span></span><span></span><span></span><span></span><span></span><span></span><span></span><span></span><span></span></div>
  <div class="contact c-left"><div>000.000.0000</div><div>info@northgatemotors.com</div></div>
  <div class="contact c-right"><div>Dummy city</div><div>Dummy country, land</div></div>
  <div class="foot-blue"></div>
  <div class="foot-dark">www.northgatemotors.com</div>
</section>

<section class="piece letter-back">
  <div class="brand light"><span class="dot" style="width:12px;height:12px"></span>Northgate Motors</div>
  <div class="contact">
    <div><span class="ico" style="width:6px;height:6px"></span>000.000.0000</div>
    <div><span class="ico" style="width:6px;height:6px"></span>info@northgatemotors.com</div>
  </div>
  <div class="foot-blue"></div>
</section>

<section class="piece letter">
  <div class="brand"><span class="dot" style="width:8px;height:8px"></span>Northgate Motors</div>
  <div class="body salute">To,<br>The<br>Director,</div>
  <div class="body p1"><p>Lorem Ipsum is simply dummy text of the printing and typesetting industry. Lorem Ipsum has been the industry's standard dummy text ever since the 1500s, when an unknown printer took a galley of type and scrambled it to make a type specimen book. It has survived not only five centuries, but also the leap into electronic typesetting, remaining essentially unchanged. It was popularised in the 1960s with the release of Letraset sheets containing Lorem Ipsum passages, and more recently with desktop publishing software like Aldus PageMaker including versions of Lorem Ipsum</p></div>
  <div class="body p2"><p>Lorem Ipsum is simply dummy text of the printing and typesetting industry. Lorem Ipsum has been the industry's standard dummy text ever since the 1500s, when an unknown printer took a galley of type and scrambled it to make a type specimen book. It has survived not only five centuries, but also the leap into electronic typesetting, remaining essentially unchanged. It was popularised in the 1960s with the release of Letraset sheets containing Lorem Ipsum passages, and more recently with desktop publishing software like Aldus PageMaker including versions of Lorem Ipsum</p></div>
  <div class="body p3"><p>Lorem Ipsum is simply dummy text of the printing and typesetting industry. Lorem Ipsum has been the industry's standard dummy text ever since the 1500s, when an unknown printer took a galley of type and scrambled it to make a type specimen book. It has survived not only five centuries, but also the leap into electronic typesetting, remaining essentially unchanged. It was popularised in the 1960s with the release of Letraset sheets containing Lorem Ipsum passages, and more recently with desktop publishing software like Aldus PageMaker including versions of Lorem Ipsum.</p></div>
  <div class="closing">Thanking you,</div>
  <div class="sign">John Doe</div>
  <div class="contact c-left">
    <div><span class="ico" style="width:6px;height:6px"></span>000.000.0000</div>
    <div><span class="ico" style="width:6px;height:6px"></span>info@northgatemotors.com</div>
  </div>
  <div class="contact c-right">
    <div><span class="ico" style="width:6px;height:6px"></span>Dummy city</div>
    <div style="padding-left:10px">Dummy country, land</div>
  </div>
  <div class="foot-blue"></div>
  <div class="foot-dark">www.northgatemotors.com</div>
</section>

<section class="piece sheet">
  <div class="brand"><span class="dot" style="width:8px;height:8px"></span>Northgate Motors</div>
  <div class="contact"><span class="ico" style="width:6px;height:6px"></span>Dummy city, Dummy country, land</div>
  <div class="foot-blue"></div>
  <div class="foot-dark">www.northgatemotors.com</div>
</section>

</body>
</html>
```